School Management website

I need page design for our school management system website

Base website is www.tavrinel.com. When the student logs in, he will reach the below pages.
You can either design with white and blue background or grey and white background

Page 1 - School Info

Header
product name("Tavrinel") in left corner
logout link in right corner

LeftMenu

Dashboard
School Info
School Settings
Staffs
Classes
Messaging
Contact Us

Footer
About link and copyright text

School Info content
The page should have breadcrumb

The content of this page will be the school profile
We have to show the school logo
Name
School Type
School Code
School Count
School Address
School phone 1&2
School Email
School Website

The page content should show edit school profile link which will take the user to another page

```html
<!DOCTYPE html>
<html lang="en">
<head>
<meta charset="utf-8">
<title>Tavrinel – School Info</title>
<link href="https://fonts.googleapis.com/css2?family=Mulish:wght@400;500;600;700&display=swap" rel="stylesheet">
<style>
  :root {
    --brand-blue: #2ba6df;
    --sky-top: #3ab0e3;
    --sky-bottom: #c9eaf9;
    --header-bg: #f7f7f7;
    --panel-bg: #ffffff;
    --ink: #333333;
    --rule: #dddddd;
    --field-bg: #f7f7f7;
    --field-line: #999999;
    --footer-bg: #404040;
    --footer-ink: #bdbdbd;
  }
  * { box-sizing: border-box; margin: 0; padding: 0; }
  html, body {
    width: 1200px; height: 827px; overflow: hidden;
    font-family: "Mulish", sans-serif; color: var(--ink);
  }
  body {
    position: relative;
    background: linear-gradient(to bottom, var(--sky-top) 89px, var(--sky-bottom) 740px);
  }
  a { text-decoration: none; color: inherit; }

  .site-header {
    position: absolute; left: 0; top: 0; width: 1200px; height: 89px;
    background: var(--header-bg); border-bottom: 1px solid #dcdcdc;
  }
  .brand {
    position: absolute; display: flex; align-items: center; gap: 8px;
    font-weight: 700; color: var(--brand-blue);
  }
  .brand-mark { width: 14px; height: 14px; background: var(--brand-blue); }
  .site-header .brand { left: 130px; top: 30px; font-size: 24px; }
  .logout {
    position: absolute; right: 130px; top: 37px;
    font-size: 12px; color: var(--brand-blue); letter-spacing: 0.3px;
  }

  .page {
    position: absolute; left: 120px; top: 89px; width: 960px; height: 651px;
    background: var(--panel-bg);
  }
  .breadcrumb {
    position: absolute; left: 10px; top: 20px; width: 940px; height: 33px;
    border-bottom: 1px solid var(--rule);
    font-size: 11px; letter-spacing: 0.2px;
  }
  .breadcrumb .sep { margin: 0 6px; font-size: 9px; }
  .breadcrumb .current { color: var(--brand-blue); }

  .side-menu { position: absolute; left: 10px; top: 68px; width: 220px; list-style: none; }
  .side-menu li {
    position: relative; height: 40px; line-height: 40px; padding-left: 16px;
    font-size: 12px; letter-spacing: 0.4px; border-bottom: 1px solid var(--rule);
  }
  .side-menu li:last-child { border-bottom: none; }
  .side-menu li.active { color: var(--brand-blue); }
  .side-menu li.active::before {
    content: ""; position: absolute; left: 1px; top: 13px;
    border-left: 5px solid var(--brand-blue);
    border-top: 7px solid transparent; border-bottom: 7px solid transparent;
  }

  .profile-card {
    position: absolute; left: 250px; top: 76px; width: 700px; height: 540px;
    border: 1px solid var(--rule);
  }
  .profile-head {
    position: absolute; left: 30px; top: 0; width: 637px; height: 99px;
    border-bottom: 1px solid var(--rule);
  }
  .profile-head .brand { left: 0; top: 42px; font-size: 22px; }
  .edit-profile {
    position: absolute; right: 0; top: 48px;
    font-size: 12px; color: var(--brand-blue); letter-spacing: 0.3px;
  }
  .profile-fields { position: absolute; left: 0; top: 114px; }
  .field { position: absolute; left: 0; width: 560px; height: 35px; }
  .field label {
    position: absolute; left: 0; width: 166px; top: 9px;
    text-align: right; font-size: 14px;
  }
  .field .value {
    position: absolute; left: 195px; top: 0; width: 358px; height: 35px;
    background: var(--field-bg); border-bottom: 1px solid var(--field-line);
    border-left: 1px solid #bbbbbb;
  }

  .site-footer {
    position: absolute; left: 0; top: 740px; width: 1200px; height: 87px;
    background: var(--footer-bg); color: var(--footer-ink); font-size: 12px;
  }
  .copyright { position: absolute; left: 130px; top: 37px; }
  .footer-links { position: absolute; right: 130px; top: 37px; }
  .footer-links .divider { margin: 0 6px; }
</style>
</head>
<body>
  <header class="site-header">
    <div class="brand"><span class="brand-mark"></span>Tavrinel</div>
    <a class="logout" href="#">LOG -OUT</a>
  </header>

  <main class="page">
    <nav class="breadcrumb">HOME<span class="sep">»</span>LOG IN<span class="sep">»</span><span class="current">SCHOOL INFO</span></nav>

    <ul class="side-menu">
      <li>DASHBOARD</li>
      <li class="active">SCHOOL INFO</li>
      <li>SCHOOL SETTINGS</li>
      <li>STAFFS</li>
      <li>CLASSES</li>
      <li>MESSAGING</li>
      <li>CONTACT US</li>
    </ul>

    <section class="profile-card">
      <div class="profile-head">
        <div class="brand"><span class="brand-mark"></span>Tavrinel</div>
        <a class="edit-profile" href="#">EDIT SCHOOL PROFILE</a>
      </div>
      <div class="profile-fields">
        <div class="field" style="top:0"><label>Name :</label><div class="value"></div></div>
        <div class="field" style="top:51px"><label>School Type :</label><div class="value"></div></div>
        <div class="field" style="top:102px"><label>School Code :</label><div class="value"></div></div>
        <div class="field" style="top:153px"><label>School Count :</label><div class="value"></div></div>
        <div class="field" style="top:204px"><label>School Address :</label><div class="value"></div></div>
        <div class="field" style="top:255px"><label>School phone 1 &amp; 2 :</label><div class="value"></div></div>
        <div class="field" style="top:306px"><label>School Email :</label><div class="value"></div></div>
        <div class="field" style="top:357px"><label>School Website :</label><div class="value"></div></div>
      </div>
    </section>
  </main>

  <footer class="site-footer">
    <p class="copyright">Copyright © 2014 | All Rights Reserved</p>
    <p class="footer-links"><a href="#">About Us</a><span class="divider">|</span><a href="#">Privacy Polcy</a></p>
  </footer>
</body>
</html>
```